Visitenkarten-Design für Lichtfeder - Zeilen von Hand zu Hand
Zielgruppe
Ich schreibe Briefe an Menschen, die mehr über sich erfahren wollen, die sich berühren lassen wollen, die an sich arbeiten möchten, die sich entfalten wollen. Ich möchte nicht den Verstand sondern das Herz ansprechen, die Selbstheilung erfahren möchten, damit sie Impulse bekommen, um ein glücklicheres Leben zu führen, das ihnen mehr entspricht.
Ich sehe mich als Mensch, der andere Menschen in ihrem Leben unterstützen möchte.
Aufgabenstellung
Die Briefe schreibe ich in Segoe Print, goldene Schrift auf gelblichem Papier, evtl auch anderes Papier, wenn die goldene Schrift passt.
Die Visitenkarte sollte Freude, Freiheit und Anerkennung des Menschen an sich ausstrahlen. Farben evtl. Bordeaux, mit vielleicht Rosa. Sie sollte jedoch nicht kitschig wirken.
Schön wäre vielleicht etwas mit Blumen oder Ornamenten, jedoch nicht zu überladen.
Als Text soll drauf sein:
Das beigefügte Logo, dann:
Berühren - Bewegen - Begeistern

```html
<!DOCTYPE html>
<html lang="de">
<head>
<meta charset="utf-8">
<title>Lichtfeder – Visitenkarte</title>
<link rel="stylesheet" href="https://fonts.googleapis.com/css2?family=Great+Vibes&family=Josefin+Sans:wght@400&family=Poiret+One&display=swap">
<style>
  :root {
    --paper: #fde3e0;
    --bordeaux: #6e1730;
    --bordeaux-deep: #5e0f27;
    --gold: #c9a043;
  }
  html, body {
    margin: 0;
    padding: 0;
    width: 1200px;
    height: 763px;
    overflow: hidden;
    background: var(--paper);
  }
  .card {
    position: relative;
    width: 1200px;
    height: 763px;
    overflow: hidden;
    background:
      radial-gradient(circle 520px at 84px 678px,
        var(--bordeaux-deep) 0%,
        rgba(110, 23, 48, 0.75) 30%,
        rgba(150, 60, 85, 0.35) 65%,
        rgba(253, 227, 224, 0) 100%),
      var(--paper);
  }
  .brand {
    position: absolute;
    left: 60px;
    top: 90px;
    font-family: "Josefin Sans", sans-serif;
    font-weight: 400;
    color: var(--bordeaux);
  }
  .brand-name {
    margin: 0;
    font-size: 136px;
    font-weight: 400;
    line-height: 1;
    letter-spacing: 4px;
    white-space: nowrap;
  }
  .brand-tagline {
    margin: 30px 0 0 310px;
    font-size: 30px;
    line-height: 1;
    letter-spacing: 2px;
    text-transform: uppercase;
    white-space: nowrap;
  }
  .motto {
    position: absolute;
    left: 560px;
    width: 620px;
    top: 438px;
    margin: 0;
    text-align: center;
    font-family: "Josefin Sans", sans-serif;
    font-size: 22px;
    letter-spacing: 2px;
    color: var(--bordeaux);
    white-space: nowrap;
  }
  .contact-name,
  .contact-line {
    position: absolute;
    left: 618px;
    width: 600px;
    margin: 0;
    text-align: center;
    white-space: nowrap;
  }
  .contact-name {
    top: 500px;
    font-family: "Poiret One", sans-serif;
    font-weight: 400;
    font-size: 64px;
    line-height: 1.1;
    letter-spacing: 2px;
    color: var(--gold);
  }
  .contact-line {
    font-family: "Great Vibes", cursive;
    line-height: 1;
    color: var(--bordeaux);
  }
  .contact-line.mail { top: 608px; font-size: 46px; }
  .contact-line.tel  { top: 660px; font-size: 44px; letter-spacing: 4px; }
  .contact-line.web  { top: 708px; font-size: 38px; letter-spacing: 2px; }
</style>
</head>
<body>
  <main class="card">
    <header class="brand">
      <h1 class="brand-name">Lichtfeder</h1>
      <p class="brand-tagline">Zeilen von Hand zu Hand</p>
    </header>

    <p class="motto">Berühren – Bewegen – Begeistern</p>

    <section class="contact">
      <h2 class="contact-name">Helene Brandtner</h2>
      <p class="contact-line mail">Mail: lichtfeder@beispielpost.de</p>
      <p class="contact-line tel">Tel: +49 170 55 214 806</p>
      <p class="contact-line web">www.helenebrandtner.de</p>
    </section>
  </main>
</body>
</html>
```